Luxury Wine Label for New Startup Winery

We need a wine label for our new winery startup. We have worked with a local designer but do not feel the resulting label / logo have the elevation required to present our brand as a luxury wine. Our winery is called "Harrowgate Vineyards" and we are focused on extremely high quality hand crafted artisan and estate wines from the Pacific Northwest.
We would like to see designs that utilize a tree line, or other imagery that represents the "Harrowgate" part of our company name. Another interesting feature could be wood grain.
A logo will be required based on your design so please design with this in mind:
This logo should be consistent with the wine bottle label design, and should be representative of our high end exclusive wine while giving a sense of place (Oregon/ Pacific Northwest.)
I will supply an image of the design we received from our local designer, PLEASE NOTE: in general we do like wood grain and tree line concepts but feel the execution was poorly done.
ATTN: Logo design should be suitable for use on: Bottles (Red wine/rose/white wine), Bussiness cards, vehicle signage, business signage, etc
P.S.:
If you have a design that is not outside the box we are still interested in seeing it.
Label is for a burgundy style bottle with a label height of 3.5 - 4" and a width of 3.5-4"
any label <= 4"x4" and >=3.5"x3.5" will be acceptable:
HOWEVER Width should be greater than or equal to height due to the bottle format
Target Market(s)
Wine enthusiasts with adequate discretionary budgets to afford $100 bottles of wine.
Industry/Entity Type
Wine / Winery
Requirements
Must have
- A sense of luxury, a feel of exclusivity, and a theme consistent with our product and brand name
Nice to have
- Tree line, wood grain or other wood themes. Serif fonts
Should not have
- anything cheesy, off topic, hard to read script fonts or anything that makes the label hard to read from a few feet away or too busy

```html
<!DOCTYPE html>
<html lang="en">
<head>
<meta charset="utf-8">
<title>Harrowgate Vineyards — Wine Labels</title>
<link rel="stylesheet" href="https://fonts.googleapis.com/css2?family=Marcellus&display=swap">
<style>
  :root {
    --page-bg: #ffffff;
    --label-bg: #fdfdfd;
    --ink: #1c1c1c;
    --frame: #2a2a2a;
    --rose: #b4547a;
    --trees-dark: #1f1f1f;
    --trees-light: #9a9a9a;
  }
  * { margin: 0; padding: 0; box-sizing: border-box; }
  html, body {
    width: 1200px;
    height: 1200px;
    overflow: hidden;
    background: var(--page-bg);
  }
  .label-sheet {
    position: relative;
    width: 1200px;
    height: 1200px;
  }
  .label {
    position: absolute;
    top: 330px;
    width: 540px;
    height: 540px;
    background: var(--label-bg);
    border: 1.5px solid var(--frame);
    font-family: "Marcellus", "Times New Roman", serif;
    color: var(--ink);
  }
  .label--syrah { left: 40px; }
  .label--rose { left: 620px; }
  .label > * {
    position: absolute;
    left: 50%;
    transform: translateX(-50%);
    white-space: nowrap;
    text-align: center;
  }
  .brand-mark {
    top: 21px;
    width: 43px;
    height: 43px;
    border: 2px solid var(--ink);
    border-radius: 50%;
  }
  .brand-name {
    top: 86px;
    font-size: 33px;
    letter-spacing: 2px;
    line-height: 36px;
  }
  .brand-sub {
    top: 123px;
    font-size: 18px;
    letter-spacing: 5px;
    line-height: 22px;
    padding-left: 5px;
  }
  .varietal {
    top: 164px;
    font-size: 43px;
    letter-spacing: 16px;
    line-height: 50px;
    padding-left: 16px;
  }
  .varietal-rule {
    top: 218px;
    width: 155px;
    height: 1.5px;
    background: var(--ink);
  }
  .tree-line {
    background: linear-gradient(180deg, var(--trees-light) 0%, var(--trees-dark) 45%, var(--trees-dark) 100%);
    clip-path: polygon(0 100%, 8% 70%, 20% 30%, 32% 5%, 45% 35%, 60% 10%, 75% 40%, 88% 60%, 100% 100%);
  }
  .label--syrah .tree-line {
    top: 240px;
    width: 165px;
    height: 165px;
  }
  .region {
    top: 438px;
    font-size: 18px;
    letter-spacing: 5px;
    line-height: 22px;
    padding-left: 5px;
  }
  .vintage {
    top: 480px;
    font-size: 23px;
    letter-spacing: 5px;
    line-height: 28px;
    padding-left: 5px;
  }
  .label--rose .varietal {
    top: 172px;
    font-size: 62px;
    letter-spacing: 10px;
    line-height: 70px;
    padding-left: 10px;
    color: var(--rose);
  }
  .label--rose .tree-line {
    top: 276px;
    width: 230px;
    height: 180px;
  }
</style>
</head>
<body>
  <main class="label-sheet">
    <section class="label label--syrah">
      <div class="brand-mark" aria-hidden="true"></div>
      <h1 class="brand-name">HARROWGATE</h1>
      <p class="brand-sub">VINEYARDS</p>
      <h2 class="varietal">SYRAH</h2>
      <div class="varietal-rule"></div>
      <div class="tree-line" role="img" aria-label="Illustration of a stand of tall evergreen trees"></div>
      <p class="region">WILLAMETTE VALLEY</p>
      <p class="vintage">2024</p>
    </section>

    <section class="label label--rose">
      <div class="brand-mark" aria-hidden="true"></div>
      <h1 class="brand-name">HARROWGATE</h1>
      <p class="brand-sub">VINEYARDS</p>
      <h2 class="varietal">ROSE</h2>
      <div class="tree-line" role="img" aria-label="Illustration of a wide tree line of evergreen trees"></div>
    </section>
  </main>
</body>
</html>
```